Business Card and Logo Color Scheme Design Contest

We are starting a new company called Lone Ridge Structural Partners and already have a logo however, the colors for the logo itself are not final and COULD be changed. I'm hoping to move AWAYfrom the gold color in the card and the logo as it seems a bit outdated. What we need help with is to find what our business color scheme will be, and then incorporate those colors into both the logo and the business card design itself. We also want to make sure we are known as "LRS" so in the future we can just refer to ourselves as "LRS" and not Lone Ridge Structural Partners. That being said, I would like to make a slight change to the logo to somehow include the letters "LRS." The logo used in the front of the card design MUST ALSO include the words "Firm No. 64307" within the logo. My vision is for the front of the card to have the information shown in the attached image. For the back of the card, I'm hoping to have something very simple. I'm envisioning a solid color with either the website (www.bridgemarkplans.com) and a simplified version of the logo. I've attached an example but I'm looking for a complete redesign. I'm looking for a slick, modern and simple design.

Industry/Entity Type

Civil Engineer

Contact Information for Business Card

Logo
Firm No. 64307
Marcus Holloway, PE
Chief Operating Officer
Email:mholloway@bridgemarkplans.com
Ph: 936.555.0142 | D: 936.555.0178 | M:210.555.0263
4187 W. Kellingham, Conroe, Texas 77301
www.bridgemarkplans.com

Requirements
Must have
• Logo
Contact Info
Nice to have
• "LRS" Incorporated in the design
Should not have
• The current color scheme

```html
<!DOCTYPE html>
<html lang="en">
<head>
<meta charset="utf-8">
<title>LRS Business Card</title>
<link rel="stylesheet" href="https://fonts.googleapis.com/css2?family=Open+Sans:wght@400;600;700&display=swap">
<style>
  :root {
    --lime: #bfd730;
    --charcoal: #414042;
    --ink: #444446;
    --paper: #ffffff;
    --backdrop: #e9e9e9;
    --rule: #8a8a8a;
  }
  * { margin: 0; padding: 0; box-sizing: border-box; }
  html, body {
    width: 1200px;
    height: 1000px;
    overflow: hidden;
    background: var(--backdrop);
    font-family: "Open Sans", Arial, sans-serif;
    color: var(--ink);
  }
  .canvas { position: relative; width: 1200px; height: 1000px; }

  .card { position: absolute; width: 678px; height: 387px; overflow: hidden; }

  /* Front */
  .card-front { left: 64px; top: 77px; background: var(--paper); }
  .person { position: absolute; left: 35px; top: 52px; }
  .person-name { font-size: 27px; font-weight: 600; line-height: 36px; }
  .person-title { font-size: 20px; font-weight: 400; line-height: 30px; }

  .brand-front { position: absolute; left: 319px; top: 58px; width: 322px; }
  .brand-row { display: flex; align-items: center; gap: 18px; }
  .brand-square { width: 58px; height: 58px; background: var(--lime); flex: none; }
  .brand-name {
    font-size: 62px; font-weight: 700; line-height: 62px; color: var(--charcoal);
    letter-spacing: 2px;
  }
  .brand-divider { height: 1px; background: var(--charcoal); margin: 10px 0 6px 76px; }
  .brand-full {
    margin-left: 76px; font-size: 13px; font-weight: 700; color: var(--charcoal);
    text-transform: uppercase; line-height: 16px; text-align: center;
  }

  .contact {
    position: absolute; left: 37px; top: 219px;
    border-left: 2px solid var(--rule);
    padding-left: 15px;
    font-size: 20px; line-height: 34.5px;
  }

  /* Back */
  .card-back { left: 451px; top: 524px; background: var(--lime); }
  .brand-back {
    position: absolute; left: 0; right: 0; top: 84px;
    display: flex; justify-content: center; align-items: center; gap: 24px;
  }
  .brand-back .brand-square { width: 96px; height: 96px; background: var(--charcoal); }
  .brand-back .brand-name { font-size: 72px; line-height: 72px; }
  .back-band {
    position: absolute; left: 0; right: 0; bottom: 0; height: 123px;
    background: var(--charcoal);
    display: flex; align-items: center; justify-content: center;
  }
  .website { color: var(--lime); font-size: 26px; font-weight: 400; }
</style>
</head>
<body>
<main class="canvas">
  <section class="card card-front" aria-label="Card front">
    <div class="person">
      <p class="person-name">Marcus Holloway, PE</p>
      <p class="person-title">Chief Operating Officer</p>
    </div>
    <div class="brand-front">
      <div class="brand-row">
        <span class="brand-square" aria-hidden="true"></span>
        <span class="brand-name">LRS</span>
      </div>
      <div class="brand-divider"></div>
      <p class="brand-full">Lone Ridge Structural Partners</p>
    </div>
    <div class="contact">
      <p>Firm No. 64307</p>
      <p>Email: mholloway@bridgemarkplans.com</p>
      <p>Ph: 936.555.0142 | D: 936.555.0178 | M:210.555.0263</p>
      <p>4187 W. Kellingham, Conroe, Texas 77301</p>
    </div>
  </section>

  <section class="card card-back" aria-label="Card back">
    <div class="brand-back">
      <span class="brand-square" aria-hidden="true"></span>
      <span class="brand-name">LRS</span>
    </div>
    <div class="back-band">
      <p class="website">www.bridgemarkplans.com</p>
    </div>
  </section>
</main>
</body>
</html>
```